New Business Card Design Project

Vorin focus is Keltrova Asset Management and Supply Chain.
We have Business Process Experts that can help you get the maximum potential out of your KLM T/7RIVA ERP. We look to understand your business and through the People, Process and Technologies to make you streamline your users digital experience.

The back of the card will be either;
- all black with the orange logo
- all orange with the black logo
- all white with the orange logo
- or make something special
The detail side, show me your best designs.
Try having the side a different colour. So if the one side is black the other is white…

Target Market(s)

Corporate Professional Business

Industry/Entity Type

Mining, Software

Contact Information for Business Card

Name, Position, brief what we do

Colors
F0912C
F2A743
F7CA91
FBE8D2
FDF5EE

Requirements
Must have
• Clear Practical Answers to Tough Challenges

```html
<!DOCTYPE html>
<html lang="en">
<head>
<meta charset="utf-8">
<title>Vorin Business Card</title>
<link href="https://fonts.googleapis.com/css2?family=Lato:wght@400;700;900&display=swap" rel="stylesheet">
<style>
  :root {
    --orange: #f47a20;
    --ink: #111111;
    --card-dark: #1e1e1e;
    --paper: #ffffff;
    --stage-top: #2b2b2b;
    --stage-bottom: #0e0e0e;
    --muted: #2a2a2a;
  }
  * { margin: 0; padding: 0; box-sizing: border-box; }
  html, body { width: 1200px; height: 875px; overflow: hidden; }
  body {
    background: linear-gradient(160deg, var(--stage-top), var(--stage-bottom));
    font-family: "Lato", sans-serif;
    position: relative;
  }
  .card {
    position: absolute;
    top: 289px;
    width: 520px;
    height: 297px;
    border-radius: 18px;
    overflow: hidden;
    box-shadow: 0 18px 40px rgba(0,0,0,0.55);
  }
  .card--back { left: 60px; background: var(--card-dark); }
  .card--front { left: 620px; background: var(--paper); }

  /* Back side */
  .back-mark {
    position: absolute;
    left: 0; right: 0; top: 88px;
    display: flex; align-items: center; justify-content: center; gap: 14px;
  }
  .mark-dot {
    width: 34px; height: 34px; border-radius: 50%;
    background: var(--orange);
  }
  .mark-name {
    font-weight: 900; font-size: 56px; color: var(--orange); letter-spacing: 1px; line-height: 1;
  }
  .back-tagline {
    position: absolute; left: 0; right: 0; bottom: 62px;
    text-align: center; color: #f2f2f2; font-size: 14px; letter-spacing: 0.4px;
  }

  /* Front side */
  .front-art { position: absolute; inset: 0; }
  .person { position: absolute; left: 44px; top: 48px; }
  .person-name {
    font-weight: 900; font-size: 30px; color: var(--ink); letter-spacing: 0.5px; line-height: 1;
  }
  .person-role { color: var(--orange); font-size: 15px; margin-top: 4px; }
  .focus {
    position: absolute; left: 44px; top: 110px;
    font-weight: 700; font-size: 11.5px; color: var(--ink);
  }
  .contact-list { position: absolute; left: 44px; top: 130px; list-style: none; }
  .contact-list li {
    display: flex; align-items: flex-start; gap: 8px;
    font-size: 11.5px; color: var(--muted); line-height: 15px;
  }
  .contact-list svg { width: 11px; height: 11px; margin-top: 2px; flex: none; fill: var(--orange); }
  .front-mark {
    position: absolute; left: 350px; top: 116px;
    display: flex; align-items: center; gap: 10px;
  }
  .front-mark .mark-dot { width: 28px; height: 28px; }
  .front-mark .mark-name { font-size: 46px; }
  .front-tagline {
    position: absolute; left: 44px; bottom: 22px;
    color: var(--paper); font-weight: 900; font-size: 14px; letter-spacing: 0.2px;
  }
</style>
</head>
<body>

<section class="card card--back" aria-label="Card back">
  <div class="back-mark">
    <span class="mark-dot"></span>
    <span class="mark-name">Vorin</span>
  </div>
  <p class="back-tagline">Clear Practical Answers to Tough Challenges</p>
</section>

<section class="card card--front" aria-label="Card front">
  <svg class="front-art" viewBox="0 0 520 297" aria-hidden="true">
    <rect x="0" y="52" width="8" height="30" fill="var(--orange)"/>
    <polygon points="0,258 300,258 330,232 372,232 372,297 0,297" fill="var(--orange)"/>
    <polygon points="448,76 520,48 520,76 458,100" fill="var(--orange)"/>
  </svg>

  <div class="person">
    <h1 class="person-name">MAREK TOLLAND</h1>
    <p class="person-role">Founder &amp; CEO</p>
  </div>

  <p class="focus">Keltrova Asset Management &amp; Supply Chain.</p>

  <ul class="contact-list">
    <li>
      <svg viewBox="0 0 12 12"><path d="M6 0a4 4 0 0 0-4 4c0 3 4 8 4 8s4-5 4-8a4 4 0 0 0-4-4zm0 5.5A1.5 1.5 0 1 1 6 2.5a1.5 1.5 0 0 1 0 3z"/></svg>
      <span>Street Address Here, City<br>State, Country, ZIP 123</span>
    </li>
    <li>
      <svg viewBox="0 0 12 12"><path d="M2.5 0.5l2 2.5-1.2 1.4a7 7 0 0 0 4.3 4.3L9 7.5l2.5 2-1.5 2C5 11.5 0.5 7 0.5 2z"/></svg>
      <span>(555) 318-2046</span>
    </li>
    <li>
      <svg viewBox="0 0 12 12"><path d="M3 0h6v12H3zM4 1.5v8h4v-8zM5.5 10.2h1v1h-1z" fill-rule="evenodd"/></svg>
      <span>(555) 318-2047</span>
    </li>
    <li>
      <svg viewBox="0 0 12 12"><path d="M0 2h12v8H0zM0.8 2.6L6 6.8l5.2-4.2v-.2H0.8z"/></svg>
      <span>info@vorinsolutions.com</span>
    </li>
    <li>
      <svg viewBox="0 0 12 12"><circle cx="6" cy="6" r="5.5"/><circle cx="6" cy="6" r="2" fill="#fff"/></svg>
      <span>vorinsolutions.com</span>
    </li>
  </ul>

  <div class="front-mark">
    <span class="mark-dot"></span>
    <span class="mark-name">Vorin</span>
  </div>

  <p class="front-tagline">Clear Practical Answers to Tough Challenges</p>
</section>

</body>
</html>
```